Company Profile
Corvane Logistics Sdn Bhd is a well established and experienced freight forwarder in Kuala Lumpur, Malaysia. We specialize in air and sea forwarding, Custom Brokerage and regulatory compliance services, inland transportation,
overseas freighting and warehousing and distribution management. With our dedicated qualified and experienced professionals, we are fully committed to serving our clients.

Our Mission
Based on the motto “Quick, Reliable and Polite”, Corvane Logistics is dedicated to upholding the following three points corporate philosophy:
1. Adhering to the principle that “the customer always comes first”.
2. Contributing to the development of the local community.
3. Making it our duty to be responsible and sincere.

Our Edge
• One-Stop Logistics Solutions
• Extensive Network Throughout Malaysia
• Highly Qualified and Experienced Pool of Professionals
• Comprehensive IT Solutions
• Innovative and Customer-focused Solutions
• Flexible and Consistent in Managing Exceptions
• Total Supply Chain Visibility

Target Market(s)

We sell the logistics services to all the industry in Malaysia. (ONE Stop Logistics Solutions)

Industry/Entity Type

Logistic

Contact Information for Business Card

I want the back of the card to be white with the logo and slogan. i would like to see the logo on the front with the general info.

Requirements
Must have
• Name, Title, Office, Cell, Fax, Email, Address, Website
Nice to have
• Modern Design Business Card

```html
<!DOCTYPE html>
<html lang="en">
<head>
<meta charset="utf-8">
<title>Corvane Logistics Stationery</title>
<link href="https://fonts.googleapis.com/css2?family=Open+Sans:wght@400;600;700&display=swap" rel="stylesheet">
<style>
  :root{
    --bg:#e7e9e9;
    --paper:#ffffff;
    --blue:#2196d9;
    --blue-light:#2aa9e2;
    --blue-deep:#1b6cc2;
    --grey:#8c8f94;
    --ink:#3a3d42;
    --ink-soft:#6b6f75;
  }
  *{box-sizing:border-box;margin:0;padding:0}
  html,body{width:1200px;height:900px;overflow:hidden;background:var(--bg)}
  body{font-family:"Open Sans",Arial,sans-serif;color:var(--ink);position:relative}

  .sheet{position:absolute;background:var(--paper);overflow:hidden;box-shadow:0 6px 18px rgba(0,0,0,.12)}
  .wave{position:absolute;left:0;top:0;width:100%;height:100%}

  .brand{position:absolute;display:flex;align-items:center;gap:6px;color:var(--blue);font-weight:700;white-space:nowrap}
  .brand-dot{border-radius:50%;background:var(--blue);flex:none}

  /* letterhead */
  .letterhead{left:330px;top:40px;width:340px;height:481px}
  .letterhead .brand{left:50%;transform:translateX(-50%);top:34px;font-size:15px}
  .letterhead .brand-dot{width:10px;height:10px}
  .letter-body{position:absolute;left:34px;right:34px;top:80px;font-size:6.6px;line-height:1.55;color:var(--ink-soft)}
  .letter-body p{margin-bottom:7px}
  .signer{position:absolute;right:40px;top:255px;font-size:6.6px;color:var(--ink-soft);text-align:right;letter-spacing:.03em}
  .signer-line{display:block;width:80px;border-top:1px solid #b9bcc0;margin:0 0 3px auto}
  .letter-footer{position:absolute;left:16px;right:24px;top:348px;display:flex;gap:12px;color:#fff;font-size:5.6px;line-height:1.5}
  .letter-footer .footer-address{flex:1.2;padding-right:10px;border-right:1px solid rgba(255,255,255,.6)}
  .letter-footer .footer-contact{flex:1}
  .letter-footer strong{font-weight:700}

  /* folder */
  .folder{left:710px;top:40px;width:460px;height:612px}
  .folder .brand{left:50%;transform:translateX(-50%);top:210px;font-size:30px}
  .folder .brand-dot{width:18px;height:18px}

  /* envelope */
  .envelope{left:330px;top:570px;width:440px;height:210px}
  .envelope .brand{left:50%;transform:translateX(-50%);top:36px;font-size:19px}
  .envelope .brand-dot{width:12px;height:12px}

  /* business cards */
  .card{width:262px;height:150px}
  .card-front{left:40px;top:330px}
  .card-back{left:40px;top:500px}
  .card .brand{font-size:12px}
  .card .brand-dot{width:8px;height:8px}
  .card-front .brand{left:16px;top:18px}
  .card-person{position:absolute;right:16px;top:16px;text-align:right}
  .card-name{font-size:10px;font-weight:700;color:var(--blue)}
  .card-title{font-size:6.5px;color:var(--ink-soft)}
  .card-office{position:absolute;left:16px;top:44px;font-size:5.6px;line-height:1.45;color:var(--ink-soft);width:120px}
  .card-office strong{color:var(--ink)}
  .card-contact{position:absolute;right:16px;top:50px;list-style:none;font-size:6px;line-height:1.55;color:var(--ink)}
  .card-contact b{color:var(--blue)}
  .card-slogan{position:absolute;left:14px;bottom:9px;font-size:6.5px;font-weight:600;letter-spacing:.08em;color:#fff}
  .card-back .brand{left:50%;transform:translateX(-50%);top:90px}
  .services-heading{position:absolute;left:14px;top:10px;font-size:7px;font-weight:700;color:var(--ink)}
  .services{position:absolute;list-style:none;font-size:5.8px;line-height:1.55;color:var(--ink)}
  .services li::before{content:"";display:inline-block;width:3px;height:3px;border-radius:50%;background:var(--ink);margin-right:3px;vertical-align:middle}
  .services-main{left:14px;top:21px}
  .services-extra{right:20px;top:28px}
</style>
</head>
<body>

<svg width="0" height="0" style="position:absolute" aria-hidden="true">
  <defs>
    <linearGradient id="blueFill" x1="0" y1="0" x2="1" y2="1">
      <stop offset="0" stop-color="#2aa9e2"/><stop offset="1" stop-color="#1b6cc2"/>
    </linearGradient>
  </defs>
</svg>

<!-- letterhead -->
<section class="sheet letterhead">
  <svg class="wave" viewBox="0 0 340 481" aria-hidden="true">
    <path d="M0 318 C110 308 230 322 340 352 L340 481 L0 481 Z" fill="url(#blueFill)"/>
    <path d="M168 481 C215 432 275 418 340 414 L340 481 Z" fill="#8c8f94"/>
    <path d="M186 481 C232 440 283 428 340 426 L340 481 Z" fill="#fff"/>
  </svg>
  <div class="brand"><span class="brand-dot"></span>Corvane Logistics</div>
  <div class="letter-body">
    <p>Dear Valued Partner,</p>
    <p>Thank you for choosing our freight forwarding services. We handle air and sea cargo, customs brokerage, inland haulage and warehousing across Malaysia, giving you one point of contact from pickup to final delivery.</p>
    <p>Our team tracks every shipment and keeps you informed at each stage, so your goods arrive on time and in good order.</p>
    <p>We look forward to working with you.</p>
    <p>Yours sincerely,</p>
  </div>
  <div class="signer"><span class="signer-line"></span>FARID AZMAN</div>
  <footer class="letter-footer">
    <div class="footer-address"><strong>CORVANE LOGISTICS SDN BHD</strong><br>No. 12B, Jalan Seroja 3,<br>42000 Port Klang,<br>Selangor Darul Ehsan, Malaysia.</div>
    <div class="footer-contact">E: info@corvane.com.my<br>T: (603) 5521 7400<br>F: (603) 5521 7401<br>GST Registration No: 000418265017</div>
  </footer>
</section>

<!-- folder -->
<section class="sheet folder">
  <svg class="wave" viewBox="0 0 460 612" aria-hidden="true">
    <path d="M0 355 C140 345 230 420 300 500 C350 560 400 600 460 612 L0 612 Z" fill="url(#blueFill)"/>
    <path d="M250 430 C320 510 380 570 460 575 L460 600 C390 596 330 540 270 470 Z" fill="#8c8f94"/>
    <path d="M272 470 C330 540 390 590 460 592 L460 605 C390 600 335 560 285 500 Z" fill="#fff"/>
  </svg>
  <div class="brand"><span class="brand-dot"></span>Corvane Logistics</div>
</section>

<!-- envelope -->
<section class="sheet envelope">
  <svg class="wave" viewBox="0 0 440 210" aria-hidden="true">
    <path d="M0 92 C90 62 170 80 250 145 C300 185 360 196 440 192 L440 210 L0 210 Z" fill="#8c8f94"/>
    <path d="M0 98 C90 68 170 86 248 152 C295 190 340 205 380 210 L0 210 Z" fill="url(#blueFill)"/>
  </svg>
  <div class="brand"><span class="brand-dot"></span>Corvane Logistics</div>
</section>

<!-- business card front -->
<section class="sheet card card-front">
  <svg class="wave" viewBox="0 0 262 150" aria-hidden="true">
    <path d="M0 104 C80 98 160 110 262 126 L262 150 L0 150 Z" fill="url(#blueFill)"/>
    <path d="M140 150 C180 138 225 130 262 128 L262 150 Z" fill="#8c8f94"/>
    <path d="M152 150 C190 141 230 136 262 135 L262 150 Z" fill="#fff"/>
  </svg>
  <div class="brand"><span class="brand-dot"></span>Corvane Logistics</div>
  <div class="card-person">
    <div class="card-name">Hadi Rosman</div>
    <div class="card-title">Operations Manager</div>
  </div>
  <div class="card-office"><strong>CORVANE LOGISTICS SDN BHD</strong><br>No. 12B, Jalan Seroja 3, 42000 Port Klang, Selangor, Malaysia.</div>
  <ul class="card-contact">
    <li><b>E:</b> hadi.rosman@corvane.com.my</li>
    <li><b>M:</b> +6012 784 3316</li>
    <li><b>T:</b> (603) 5521 7400</li>
    <li><b>F:</b> (603) 5521 7401</li>
    <li><b>W:</b> www.corvane.com.my</li>
  </ul>
  <div class="card-slogan">ONE STOP LOGISTICS SOLUTIONS</div>
</section>

<!-- business card back -->
<section class="sheet card card-back">
  <svg class="wave" viewBox="0 0 262 150" aria-hidden="true">
    <path d="M0 114 C80 110 160 120 262 132 L262 150 L0 150 Z" fill="url(#blueFill)"/>
    <path d="M140 150 C180 140 225 134 262 132 L262 150 Z" fill="#8c8f94"/>
    <path d="M152 150 C190 143 230 139 262 138 L262 150 Z" fill="#fff"/>
  </svg>
  <div class="services-heading">We're Specialise In</div>
  <ul class="services services-main">
    <li>International Shipping (Air/Sea)</li>
    <li>Supply Chain Management</li>
    <li>Tax Exemption Consultancy</li>
    <li>Transportation / Haulage</li>
    <li>Consolidation - FCL/LCL</li>
    <li>Project Management</li>
  </ul>
  <ul class="services services-extra">
    <li>Packing</li>
    <li>Marine Insurance</li>
    <li>Warehousing</li>
    <li>Distribution</li>
    <li>Custom Brokerage</li>
    <li>Door to Door</li>
  </ul>
  <div class="brand"><span class="brand-dot"></span>Corvane Logistics</div>
  <div class="card-slogan">ONE STOP LOGISTICS SOLUTIONS</div>
</section>

</body>
</html>
```